I need a label design to go on our jars of honey. Our company is called Quillbrook Honey Co. The type of honey is called Marram Glade Honey. The jars are 1kg. Attached is the label size. Left hand side needs to have nutritional info... as attached. Middle section is our company name, honey type, 1kg & Whangamata, NZ. Right hand side needs to have info as per photo (raw honey etc). I would like to upload more pictures... but I’m unsure how to do this? Thanks, Noreen

Target Market(s)

Honey consumers... families

Industry/Entity Type

Food Production

Colors

Designer to choose colors to be used in the design.

Requirements
Must have
• Nutritional info as per upload
• Type of honey & company name as per upload
• 1kg
• Address
Nice to have
• Similar fonts to upload.
• Possibly background image... floral or beach... very faint though.

```html
<!DOCTYPE html>
<html lang="en">
<head>
<meta charset="utf-8">
<title>Quillbrook Honey Co. – Marram Glade Honey label, back panel</title>
<link href="https://fonts.googleapis.com/css2?family=Roboto:ital,wght@0,300;1,300&display=swap" rel="stylesheet">
<style>
  :root {
    --bg-dark: #1f1d14;
    --bg-warm: #2b2219;
    --bloom: #6a4330;
    --ink: #ffffff;
    --rule: #ffffff;
    --label-ink: #111111;
  }
  * { margin: 0; padding: 0; box-sizing: border-box; }
  html, body { width: 1200px; height: 1200px; overflow: hidden; }
  body {
    position: relative;
    background: radial-gradient(ellipse at 30% 10%, var(--bg-warm) 0%, var(--bg-dark) 70%);
    color: var(--ink);
    font-family: "Roboto", Helvetica, Arial, sans-serif;
    font-weight: 300;
  }
  .floral-backdrop {
    position: absolute;
    left: 950px; top: 240px;
    width: 400px; height: 660px;
    border-radius: 50%;
    background: radial-gradient(ellipse at 50% 50%, rgba(106,67,48,0.55) 0%, rgba(90,58,38,0.3) 45%, rgba(31,29,20,0) 75%);
  }
  .origin-note {
    position: absolute;
    left: 0; width: 960px; top: 50px;
    text-align: center;
    font-style: italic;
    font-size: 35px;
    line-height: 44px;
  }
  .nutrition-panel {
    position: absolute;
    left: 126px; top: 149px;
    width: 681px; height: 666px;
    border: 2.4px solid var(--rule);
  }
  .nutrition-head {
    height: 123px;
    border-bottom: 2.4px solid var(--rule);
    padding: 20px 14px 0;
    font-size: 24px;
    line-height: 32px;
    letter-spacing: -0.8px;
  }
  .nutrition-table { width: 100%; border-collapse: collapse; table-layout: fixed; }
  .nutrition-table th {
    height: 91px;
    text-align: left;
    vertical-align: top;
    padding-top: 20px;
    font-weight: 300;
    font-size: 23px;
    line-height: 31px;
    letter-spacing: -0.9px;
    border-bottom: 2.4px solid var(--rule);
    white-space: nowrap;
  }
  .nutrition-table th.col-serving { border-right: 2.4px solid var(--rule); padding-left: 283px; }
  .nutrition-table th.col-100g { padding-left: 16px; }
  .nutrition-table td {
    height: 64.2px;
    font-size: 28px;
    letter-spacing: -0.4px;
  }
  .nutrition-table .w-nutrient { width: 283px; }
  .nutrition-table .w-serving { width: 193px; }
  .nutrition-table td.nutrient { padding-left: 15px; }
  .nutrition-table td.per-100g { padding-left: 17px; }
  .storage-note {
    position: absolute;
    left: 0; width: 960px; top: 854px;
    text-align: center;
    font-style: italic;
    font-size: 32px;
    line-height: 41px;
  }
  .batch-box {
    position: absolute;
    left: 134px; top: 966px;
    width: 696px; height: 189px;
    background: #ffffff;
    color: var(--label-ink);
    padding: 22px 16px;
    font-style: italic;
    font-size: 32px;
    line-height: 41px;
  }
  .brand-block {
    position: absolute;
    left: 880px; width: 300px; top: 150px;
    text-align: center;
  }
  .brand-name {
    font-size: 34px;
    line-height: 44px;
  }
  .honey-type {
    position: absolute;
    left: 880px; width: 300px; top: 540px;
    text-align: center;
    font-size: 46px;
    line-height: 56px;
  }
</style>
</head>
<body>
  <div class="floral-backdrop" role="img" aria-label="Faint photograph of a flower in warm brown tones"></div>

  <p class="origin-note">100% New Zealand Honey<br>No added ingredients</p>

  <section class="nutrition-panel">
    <div class="nutrition-head">
      NUTRITIONAL INFORMATION<br>
      Serving per package: 100<br>
      Serving size: 10g
    </div>
    <table class="nutrition-table">
      <colgroup><col class="w-nutrient"><col class="w-serving"><col></colgroup>
      <tr>
        <th class="col-serving" colspan="2">Average Quantity<br>per Serving</th>
        <th class="col-100g">Average Quantity<br>per 100g</th>
      </tr>
      <tr><td class="nutrient">Energy</td><td class="per-serving">134kj</td><td class="per-100g">1340kj</td></tr>
      <tr><td class="nutrient">Protein</td><td class="per-serving">0.04g</td><td class="per-100g">0.4g</td></tr>
      <tr><td class="nutrient">Fat Total</td><td class="per-serving">0g</td><td class="per-100g">0g</td></tr>
      <tr><td class="nutrient">- saturated</td><td class="per-serving">0g</td><td class="per-100g">0g</td></tr>
      <tr><td class="nutrient">Carbohydrate</td><td class="per-serving">7.9g</td><td class="per-100g">79.6g</td></tr>
      <tr><td class="nutrient">- sugars</td><td class="per-serving">7.8g</td><td class="per-100g">78.1g</td></tr>
      <tr><td class="nutrient">Sodium</td><td class="per-serving">1.2mg</td><td class="per-100g">12mg</td></tr>
    </table>
  </section>

  <p class="storage-note">Store upright in a cool, dry place. No refrigeration needed.<br>Not recommended for infants below the age of 12 months.</p>

  <div class="batch-box">
    Best before:<br>
    RMP:<br>
    Batch No:
  </div>

  <div class="brand-block">
    <p class="brand-name">Quillbrook<br>Honey Co.</p>
  </div>
  <p class="honey-type">Marram Glade<br>Honey</p>
</body>
</html>
```